Business Card and Logo tweak for a Language Boarding School

we are a boadring langauge school for under 18 international student.
We call ourselves " TWSC" - Tarravale Worldwide Studies Centre
We are one of the RV "rosewood venture" Melbourne campus for RV high school preparation program.

our address is 19 Tolley Road Brighton 3186
Ph: 03 84210563
Email: info@mytwsc.com
Website: www.mytwsc.com

We have our TWSC logo, but not very satisfied. May be you can tweak it furhter with the fond or formations.

Basically the business card list all relevant info on one side and list all our programs on the other side.

The program we have:
ELICOS with Boarding for U18 Students
HSP-High School Preparation Program
PSP- Primary School Preparation Program
Junior Holiday Program & Study Tours
After School Tutoring
Student Wellbeing and Counselling

```html
<!DOCTYPE html>
<html lang="en">
<head>
<meta charset="utf-8">
<title>TWSC Business Card</title>
<link href="https://fonts.googleapis.com/css2?family=Raleway:wght@400;500&family=Open+Sans:wght@700&display=swap" rel="stylesheet">
<style>
  :root {
    --backdrop: #4b4a4d;
    --card: #ffffff;
    --card-shade: #ececee;
    --ink: #231f20;
    --icon: #2f3452;
    --band-black: #0b0b0b;
    --band-teal: #6fcbd3;
    --band-lime: #c8dc3c;
    --band-red: #ec1a45;
    --band-orange: #f7a51f;
    --band-purple: #5a2d84;
  }
  * { margin: 0; padding: 0; box-sizing: border-box; }
  html, body { width: 800px; height: 1200px; overflow: hidden; }
  body {
    background: var(--backdrop);
    position: relative;
    font-family: "Raleway", sans-serif;
    color: var(--ink);
  }
  .card {
    position: absolute;
    left: 50px;
    width: 700px;
    height: 400px;
    background: radial-gradient(ellipse at 45% 40%, var(--card) 55%, var(--card-shade) 100%);
    box-shadow: 0 14px 30px rgba(0,0,0,0.35);
    overflow: hidden;
  }
  .card--front { top: 126px; }
  .card--back { top: 674px; }

  .colour-band {
    position: absolute;
    left: 0; bottom: 0;
    width: 100%; height: 10px;
    display: flex;
  }
  .colour-band span { flex: 1; }
  .band-black { background: var(--band-black); }
  .band-teal { background: var(--band-teal); }
  .band-lime { background: var(--band-lime); }
  .band-red { background: var(--band-red); }
  .band-orange { background: var(--band-orange); }
  .band-purple { background: var(--band-purple); }

  .brand {
    position: absolute;
    display: flex;
    align-items: center;
  }
  .brand-dot {
    border-radius: 50%;
    background: var(--ink);
    flex: none;
  }
  .brand-name {
    font-weight: 500;
    text-transform: uppercase;
    color: var(--ink);
    line-height: 0.9;
  }
  .brand--front { left: 52px; top: 90px; gap: 60px; }
  .brand--front .brand-dot { width: 50px; height: 50px; }
  .brand--front .brand-name { font-size: 22px; }
  .brand--back { left: 277px; top: 313px; gap: 40px; }
  .brand--back .brand-dot { width: 29px; height: 29px; }
  .brand--back .brand-name { font-size: 13.5px; }

  .contact-list {
    position: absolute;
    left: 50px;
    top: 259px;
    list-style: none;
  }
  .contact-list li {
    display: flex;
    align-items: center;
    gap: 10px;
    height: 27.8px;
    font-size: 17px;
    letter-spacing: 0.2px;
  }
  .contact-list svg { width: 15px; height: 15px; flex: none; }

  .programs-title {
    position: absolute;
    left: 33px;
    top: 60px;
    font-family: "Open Sans", sans-serif;
    font-weight: 700;
    font-size: 18.5px;
    text-decoration: underline;
    text-underline-offset: 3px;
    letter-spacing: -0.2px;
  }
  .program-list {
    position: absolute;
    list-style: none;
    font-size: 16px;
    line-height: 20px;
  }
  .program-list li {
    position: relative;
    padding-left: 12px;
    margin-bottom: 19px;
  }
  .program-list li::before {
    content: "•";
    position: absolute;
    left: 0;
    top: -1px;
    font-size: 16px;
  }
  .program-list--left { left: 33px; top: 104px; }
  .program-list--right { left: 274px; top: 104px; }
  .program-list--right .wide { line-height: 25px; }
</style>
</head>
<body>

<section class="card card--front" aria-label="Business card front">
  <div class="brand brand--front">
    <span class="brand-dot"></span>
    <p class="brand-name">Tarravale<br>Worldwide<br>Studies<br>Centre</p>
  </div>

  <ul class="contact-list">
    <li>
      <svg viewBox="0 0 16 16" aria-hidden="true"><circle cx="8" cy="8" r="8" fill="var(--icon)"/><path d="M5.2 4.2l1.6 1.8-.8 1c.6 1.2 1.4 2 2.6 2.6l1-.8 1.8 1.6-.9 1.3C7.6 11.4 4.6 8.4 4.3 5z" fill="#fff"/></svg>
      <span>03 84210563</span>
    </li>
    <li>
      <svg viewBox="0 0 16 16" aria-hidden="true"><circle cx="8" cy="8" r="8" fill="var(--icon)"/><rect x="4" y="5.3" width="8" height="5.4" fill="#fff"/><path d="M4 5.3l4 3 4-3" stroke="var(--icon)" stroke-width="0.9" fill="none"/></svg>
      <span>info@mytwsc.com</span>
    </li>
    <li>
      <svg viewBox="0 0 16 16" aria-hidden="true"><circle cx="8" cy="8" r="8" fill="var(--icon)"/><circle cx="8" cy="8" r="4.2" fill="none" stroke="#fff" stroke-width="1"/><path d="M3.8 8h8.4M8 3.8v8.4M5.5 5.5h5M5.5 10.5h5" stroke="#fff" stroke-width="0.8"/></svg>
      <span>www.mytwsc.com</span>
    </li>
    <li>
      <svg viewBox="0 0 16 16" aria-hidden="true"><circle cx="8" cy="8" r="8" fill="var(--icon)"/><path d="M4 8.2L8 4.6l4 3.6V12H9.3V9.5H6.7V12H4z" fill="#fff"/></svg>
      <span>19 Tolley Road, Kellmoor 3299</span>
    </li>
  </ul>

  <div class="colour-band" aria-hidden="true">
    <span class="band-black"></span><span class="band-teal"></span><span class="band-lime"></span><span class="band-red"></span><span class="band-orange"></span><span class="band-black"></span><span class="band-purple"></span>
  </div>
</section>

<section class="card card--back" aria-label="Business card back">
  <h2 class="programs-title">THE PROGRAM WE HAVE:</h2>

  <ul class="program-list program-list--left">
    <li>ELICOS with Boarding<br>&nbsp;for U18 Students</li>
    <li>HSP-High School<br>Preparation Program</li>
    <li>PSP- Primary School<br>Preparation Program</li>
  </ul>

  <ul class="program-list program-list--right">
    <li>Junior Holiday Program<br>&amp; Study Tours</li>
    <li>After School Tutoring</li>
    <li class="wide">Student Wellbeing and<br>Counselling</li>
  </ul>

  <div class="brand brand--back">
    <span class="brand-dot"></span>
    <p class="brand-name">Tarravale<br>Worldwide<br>Studies<br>Centre</p>
  </div>

  <div class="colour-band" aria-hidden="true">
    <span class="band-black"></span><span class="band-teal"></span><span class="band-lime"></span><span class="band-red"></span><span class="band-orange"></span><span class="band-black"></span><span class="band-purple"></span>
  </div>
</section>

</body>
</html>
```